We need a professional contract designs with our logo

We need a contract designed on a form with our logo etc to make it look more professional and not just a word document

Also we need a cover for the contract too.

Industry/Entity Type

It Professional

```html
<!DOCTYPE html>
<html lang="en">
<head>
<meta charset="utf-8">
<title>Tenancy Agreement – Page 4</title>
<link rel="stylesheet" href="https://fonts.googleapis.com/css2?family=Lato:wght@400;700&display=swap">
<style>
  :root {
    --page-purple: #6c2a6f;
    --notice-bg: #ffffff;
    --notice-ink: #5a2466;
    --body-ink: #ffffff;
  }
  * { margin: 0; padding: 0; box-sizing: border-box; }
  html, body { width: 849px; height: 1200px; overflow: hidden; }
  body {
    background: var(--page-purple);
    font-family: "Lato", "Gill Sans", sans-serif;
    position: relative;
  }
  .notice-box {
    position: absolute;
    left: 40px; top: 40px;
    width: 768px; height: 250px;
    background: var(--notice-bg);
    color: var(--notice-ink);
    padding: 14px 24px 0 24px;
    font-size: 10.3px;
    line-height: 12.3px;
  }
  .notice-box h2 {
    font-size: 11px;
    font-weight: 700;
    margin-bottom: 1px;
  }
  .notice-box h2 + ol { margin-bottom: 9px; }
  .notice-box ol { list-style: none; }
  .notice-box li { padding-left: 10px; text-indent: -10px; }

  .terms {
    position: absolute;
    top: 312px;
    color: var(--body-ink);
    font-size: 9.9px;
    line-height: 12.1px;
  }
  .terms-left { left: 40px; width: 378px; }
  .terms-right { left: 455px; width: 355px; }
  .terms h3 { font-size: 10.2px; font-weight: 700; }
  .clause { padding-left: 10px; text-indent: -10px; }
  .clause.l2 { padding-left: 20px; text-indent: -10px; }
  .clause.l3 { padding-left: 40px; text-indent: -17px; }
  .clause.sub { padding-left: 23px; text-indent: -13px; }

  .page-number {
    position: absolute;
    right: 40px; top: 1170px;
    color: var(--body-ink);
    font-size: 14px;
  }
  .page-number strong { font-weight: 700; }
</style>
</head>
<body>

<section class="notice-box">
  <h2>IMPORTANT NOTICE TO LANDLORDS:</h2>
  <ol>
    <li>1. The details of ‘The LANDLORD’ near the top of this Agreement must include an address for the Landlord in England or Wales as well as his/her name, or all names in the case of joint Landlords.</li>
    <li>2. Always remember to give the written Notice Requiring Possession to the Tenant at least two clear months before the end of the Term if you want the Tenant to vacate.</li>
    <li>3. Before granting the tenancy agreement, you should check whether your chosen deposit scheme provider requires you to insert any additional terms concerning the deposit into the tenancy agreement or to alter or delete any of the terms appearing in the form below. Details of the websites of the scheme providers are set out in Note 4 for tenants below. Currently only The Rental Deposit Scheme has such requirements.</li>
  </ol>
  <h2>IMPORTANT NOTICE TO TENANTS:</h2>
  <ol>
    <li>1. In general, if you currently occupy this Property under a protected or statutory tenancy and you give it up to take a new tenancy of the same or other accommodation owned by the same Landlord, that tenancy cannot be an Assured Shorthold Tenancy and this Agreement is not appropriate.</li>
    <li>2. If you currently occupy this Property under an Assured Tenancy which is not an Assured Shorthold Tenancy your Landlord is not permitted to grant you an Assured Shorthold Tenancy of this Property or of alternative property and this Agreement is not appropriate.</li>
    <li>3. In England, if the total amount of rent exceeds £100,000 (£25,000 in Wales) per annum, an Assured Shorthold Tenancy cannot be created and this Agreement is not appropriate.</li>
    <li>4. Further information about the Government-authorised Tenancy Deposit Schemes can be obtained from their websites: The Deposit Safeguard Service at www.depositsafeguard.example, Secure Deposits at www.securedeposits.example and The Rental Deposit Scheme at www.rentaldisputes.example.</li>
    <li>5. If your tenancy starts after 1 October 2008, your landlord should provide you with an Energy Performance Certificate.</li>
  </ol>
</section>

<section class="terms terms-left">
  <h3>Terms and Conditions</h3>
  <p class="clause">1. This Agreement is intended to create an assured shorthold tenancy as defined in the Housing Act 1988, as amended by the Housing Act 1996, and the provisions for the recovery of possession by the Landlord in that Act apply accordingly. The Tenant understands that the Landlord will be entitled to recover possession of the Property at the end of the Term. Under this Agreement, the Tenant will have an exclusive tenancy of his Designated Room and will have a licence, in common with any other occupiers of the Property to use such Shared Parts of the Property as are not exclusively let to other occupiers and subject to any other restrictions as the Landlord may from time to time notify to the Tenant in writing.</p>
  <h3>2. The Tenant’s obligations:</h3>
  <p class="clause l2">2.1 To pay the Rent at the times and in the manner set out above.</p>
  <p class="clause l2">2.2 To make a proportionate contribution to the costs of all charges in respect of any electric, gas, water and telephone or televisual services used at or supplied to the Property and Council Tax or any similar property tax that might be charged in addition to or replacement of it during the Term.</p>
  <p class="clause l2">2.3 To keep the items on the Inventory and the interior of the Property in a good and clean state and condition and not damage or injure the Designated Room and Shared Parts of the Property or the items on the Inventory (fair wear and tear excepted).</p>
  <p class="clause l2">2.4 To yield up the Property and the items on the Inventory at the end of the Term in the same clean state and condition it/they was/were in at the beginning of the Term (but the Tenant will not be responsible for fair wear and tear caused during normal use of the Property and the items on the Inventory or for any damage covered by and recoverable under the insurance policy effected by the Landlord under clause 3.2 or for any damage to the Shared Parts of the Property and its contents caused by other tenants and/or their visitors).</p>
  <p class="clause l2">2.5 Not make any alteration or addition to the Property nor do any redecoration or painting of the Property without the Landlord’s prior written consent (consent not to be withheld unreasonably).</p>
  <p class="clause l2">2.6 Not do anything on or at the Property which:</p>
  <p class="clause l3">(a) may be or become a nuisance or annoyance to any other occupiers of the Property or owners or occupiers of adjoining or nearby premises;</p>
  <p class="clause l3">(b) is illegal or immoral;</p>
  <p class="clause l3">(c) may in any way affect the validity of the insurance of the Property and the items listed on the Inventory or cause an increase in the premium payable by the Landlord.</p>
  <p class="clause l3">(d) will cause any blockages in the drainage system and in the case of breach of this clause the Tenant to be responsible for the reasonable cost of such repair or other works which will be reasonably required.</p>
  <p class="clause l2">2.7 Not without the Landlord’s prior consent (consent not to be withheld unreasonably) allow or keep any pet or any kind of animal at the Property.</p>
  <p class="clause l2">2.8 Not use or occupy the Property in any way whatsoever other than as a private residence.</p>
  <p class="clause l2">2.9 Not assign, sublet, charge or part with or share possession or occupation of the Property (but see clause 4.1 below).</p>
  <p class="clause l2">2.10 To allow the Landlord or anyone with the Landlord’s written permission to enter the Property [Designated Room] at reasonable times of the day to inspect its condition and state of repair, carry out any necessary repairs and gas inspections, or during the last month of the Term, show the Property to prospective new tenants, provided the Landlord has given 24 hours’ prior written notice (except in emergency) and to further permit the Landlord to freely access the Shared Parts of the Property at any time.</p>
  <p class="clause l2">2.11 To pay the Landlord’s reasonable costs reasonably incurred as a result of any breaches by the tenant of his obligations under this Agreement.</p>
  <p class="clause l2">2.12 To pay interest at the rate of 4% above the Central Bank base rate from time to time prevailing on any rent or other money lawfully due from the Tenant under this Agreement which remains unpaid for more than 14 days, interest to be paid from the date the payment fell due until payment.</p>
  <p class="clause l2">2.13 To provide the Landlord with a forwarding address when the tenancy comes to an end and to remove all rubbish and all personal items (including the Tenant’s own furniture and equipment) from the Designated Room and Shared Parts of the Property before leaving.</p>
</section>

<section class="terms terms-right">
  <h3>3. The Landlord’s obligations:</h3>
  <p class="clause l2">3.1 The Landlord agrees that the Tenant may live in the Designated Room and Shared Parts of the Property without unreasonable interruption from the Landlord or any person rightfully claiming under or in trust for the Landlord.</p>
  <p class="clause l2">3.2 To insure the Property and the items listed on the Inventory and use all reasonable efforts to arrange for any damage caused by an insured risk to be remedied as soon as possible and to provide a copy of the insurance policy to the Tenant if requested.</p>
  <p class="clause l2">3.3 To keep in repair (where provided by the Landlord)</p>
  <p class="clause l3">3.3.1 the structure and exterior of the Property (including drains gutters and external pipes)</p>
  <p class="clause l3">3.3.2 the installations at the Property for the supply of water, sewage, gas and electricity and for sanitation (including basins, sinks, baths and sanitary conveniences)</p>
  <p class="clause l3">3.3.3 the installations at the Property for space heating and heating water.</p>
  <p class="clause l2">3.4 But the Landlord will not be required to</p>
  <p class="clause l3">3.4.1 carry out works for which the Tenant is responsible by virtue of his duty to use the Property in a tenant-like manner</p>
  <p class="clause l3">3.4.2 reinstate the Property in the case of damage or destruction if the insurers refuse to pay out the insurance money due to anything the Tenant has done or failed to do</p>
  <p class="clause l3">3.4.3 rebuild or reinstate the Property in the case of destruction or damage of the Property by a risk not covered by the policy of insurance effected by the Landlord.</p>
  <p class="clause l2">3.5 If the property is a flat or maisonette within a larger building then the Landlord will be under similar obligations for the rest of the building but only insofar as any disrepair will affect the Tenants enjoyment of the Property and insofar as the Landlord is legally entitled to enter the relevant part of the larger building and carry out the required works or repairs.</p>
  <p class="clause l2">3.6 To arrange for the Tenant’s Deposit to be protected by an authorised Tenancy Deposit Scheme in accordance with the provisions of the Housing Act 2004 within 14 days of receipt, and to comply with the rules of the Tenancy Deposit Scheme at all times.</p>
  <h3>4. Ending this Agreement</h3>
  <p class="clause l2">4.1 The Tenant cannot normally end this Agreement before the end of the Term. However after the first three months of the Term, if the Tenant can find a suitable alternative tenant, and provided this alternative tenant is acceptable to the Landlord (the Landlord’s approval not to be unreasonably withheld) the Tenant may give notice to end the tenancy on a date at least one month from the date that such approval is given by the Landlord. On the expiry of such notice, and upon (i) payment by the Tenant to the Landlord of the reasonable expenses reasonably incurred by the Landlord in granting the necessary approval and in granting any new tenancy to the alternative tenant, and (ii) the execution by the alternative tenant of a new tenancy agreement in the form of this Agreement for a period of 6 months or for a period not less than the unexpired portion of the term of this Agreement (if that be greater than 6 months), or for such other period as the Landlord shall approve, this tenancy shall end. The Landlord may ask the Tenant to enter into a guarantee in respect of the tenancy granted to the alternative tenant.</p>
  <p class="clause l2">4.2 If the Tenant stays on after the end of the fixed term, his tenancy will continue but will run from month to month or week to week (a ‘periodic tenancy’). This periodic tenancy can be ended by the Tenant giving at least one month’s written notice to the Landlord, the notice to expire at the end of a rental period.</p>
  <p class="clause l2">4.3 If at any time</p>
  <p class="clause l3">4.3.1 any part of the Rent is outstanding for 21 days after becoming due (whether formally demanded or not) and/or</p>
  <p class="clause l3">4.3.2 there is any breach, non-observance or non-performance by the Tenant of any covenant or other term of this Agreement which has been notified in writing to the Tenant and the Tenant has failed within a reasonable period of time to remedy the breach and/or pay reasonable compensation to the Landlord for the breach and/or</p>
  <p class="clause l3">4.3.3 any of the grounds set out as Grounds 2, 8 or Grounds 10-15 (inclusive) (which relate to breach of any obligation by a Tenant) contained in the Housing Act 1988 Schedule 2 apply the Landlord may recover possession of the Property and this Agreement shall</p>
</section>

<footer class="page-number"><strong>4</strong> | Page</footer>

</body>
</html>
```